Flyers

Modify Existing Flyer and create another for exterior company
Updates

Previous Brief has been updated- we want to update this existing one also

Target Market(s)

Exterior Remodeling Customers

Industry/Entity Type

Remodeling/Construction

```html
<!DOCTYPE html>
<html lang="en">
<head>
<meta charset="utf-8">
<title>Northvale Remodeling Flyer</title>
<link rel="stylesheet" href="https://fonts.googleapis.com/css2?family=Poppins:wght@300;400;600;700&display=swap">
<style>
  :root {
    --page-bg: #f2f2f2;
    --brand-blue: #2272bb;
    --brand-sky: #2aa3dc;
    --accent-yellow: #ffd200;
    --accent-orange: #f0582a;
    --accent-red: #d92a2a;
    --ink: #1d1d1d;
    --paper: #ffffff;
    --kitchen-teal: #46bfd3;
    --bath-warm: #d6ae82;
  }
  * { margin: 0; padding: 0; box-sizing: border-box; }
  html, body { width: 1200px; height: 1200px; overflow: hidden; }
  body { background: var(--page-bg); font-family: "Poppins", sans-serif; position: relative; }

  .flyer {
    position: absolute; left: 300px; top: 153px;
    width: 618px; height: 866px;
    background: var(--paper);
    box-shadow: 2px 3px 6px rgba(0,0,0,0.25);
    overflow: hidden;
  }

  /* Header */
  .header {
    position: absolute; left: 0; top: 0; width: 618px; height: 94px;
    background: linear-gradient(90deg, var(--brand-blue), var(--brand-sky));
  }
  .brand {
    position: absolute; left: 43px; top: 36px;
    display: flex; align-items: center; gap: 7px;
    color: #fff; font-weight: 600; line-height: 1.15;
  }
  .brand-mark { width: 12px; height: 12px; background: var(--accent-orange); }
  .brand-name { font-size: 12px; letter-spacing: 0.5px; }
  .brand-name small { display: block; font-size: 7.5px; letter-spacing: 0.6px; }
  .cta {
    position: absolute; right: 42px; top: 36px; text-align: center;
    color: #fff; font-weight: 300; font-size: 10px; line-height: 1.3;
  }
  .cta .free { color: var(--accent-orange); text-decoration: underline; }
  .cta .phone { display: block; font-weight: 700; font-size: 16px; margin-top: 1px; letter-spacing: 0.3px; }

  /* Hero */
  .hero { position: absolute; left: 0; top: 94px; width: 618px; height: 316px; }
  .hero svg { position: absolute; left: 0; top: 0; }
  .hero-headline { position: absolute; left: 42px; top: 42px; color: #fff; line-height: 1.2; }
  .hero-headline .kicker { color: var(--accent-yellow); font-size: 11.5px; font-weight: 400; }
  .hero-headline .title { font-size: 18px; font-weight: 600; }
  .hero-headline .title.yellow { color: var(--accent-yellow); font-weight: 700; }
  .hero-headline .title .or { font-weight: 400; }
  .hero-tagline { position: absolute; left: 310px; top: 249px; color: #fff; line-height: 1.1; }
  .hero-tagline .big { font-size: 21px; font-weight: 700; letter-spacing: 0.2px; }
  .hero-tagline .sub { font-size: 11.5px; font-weight: 400; letter-spacing: 0.3px; }
  .hero-rule { position: absolute; left: 0; top: 410px; width: 618px; height: 1.5px; background: var(--accent-orange); }

  /* Services */
  .service { position: absolute; width: 240px; }
  .service-icon { position: absolute; left: -35px; top: -7px; }
  .service h2 {
    color: var(--brand-blue); font-size: 12px; font-weight: 700; letter-spacing: 1px;
    line-height: 12px; white-space: nowrap;
  }
  .service p {
    font-size: 8.2px; color: var(--ink); line-height: 9.4px; margin-top: 5px; white-space: nowrap;
  }
  .service ul { list-style: none; margin-top: 6px; }
  .service li {
    font-size: 7.7px; color: #333; font-weight: 300; line-height: 11.1px;
    padding-left: 10px; position: relative; white-space: nowrap;
  }
  .service li::before {
    content: ""; position: absolute; left: 2px; top: 3.5px; width: 4px; height: 4px; background: var(--brand-blue);
  }
  .service-photo { position: absolute; }
  .photo-framed {
    border-top: 2px solid var(--brand-blue); border-left: 2px solid var(--brand-blue);
    border-top-left-radius: 12px;
  }
  .photo-kitchen { background: linear-gradient(135deg, #f4f4f2, #d7d1c8 60%, #b07c4e); }
  .photo-addition { background: linear-gradient(160deg, #6a5240, #a7a49b 50%, #3e3a33); border-top-left-radius: 10px; }
  .photo-bath { background: linear-gradient(135deg, #3a2d25, #9b8a73 55%, #e8e5de); }
  .photo-deck { background: linear-gradient(160deg, #7a8a6a, #9a6a55 50%, #4e6b35); }

  /* Footer */
  .footer {
    position: absolute; left: 0; top: 820px; width: 618px; height: 46px;
    background: var(--brand-blue); color: #fff; text-align: center;
    font-size: 18px; font-weight: 700; letter-spacing: 2px; line-height: 46px;
  }
</style>
</head>
<body>
<main class="flyer">
  <header class="header">
    <div class="brand">
      <span class="brand-mark"></span>
      <span class="brand-name">NORTHVALE<small>ROOFING AND EXTERIORS</small></span>
    </div>
    <div class="cta">
      CALL TODAY FOR YOUR<br><span class="free">FREE</span> ESTIMATE
      <span class="phone">555-014-2290</span>
    </div>
  </header>

  <section class="hero">
    <svg width="618" height="316" viewBox="0 0 618 316">
      <defs>
        <linearGradient id="kitchenTone" x1="0" y1="0" x2="0" y2="1">
          <stop offset="0" stop-color="#2c9fc7"/>
          <stop offset="0.55" stop-color="#46bfd3"/>
          <stop offset="1" stop-color="#8a6a4e"/>
        </linearGradient>
        <linearGradient id="bathTone" x1="0" y1="0" x2="1" y2="1">
          <stop offset="0" stop-color="#eddcc4"/>
          <stop offset="0.5" stop-color="#d6ae82"/>
          <stop offset="1" stop-color="#b7875a"/>
        </linearGradient>
      </defs>
      <polygon points="0,0 411,0 209,316 0,316" fill="url(#kitchenTone)" role="img" aria-label="Modern kitchen with island and bar stools"/>
      <polygon points="411,0 618,0 618,316 209,316" fill="url(#bathTone)" role="img" aria-label="Bright bathroom with freestanding tub and glass shower"/>
      <line x1="411" y1="0" x2="209" y2="316" stroke="#fff" stroke-width="3"/>
      <polygon points="9,36 349,36 300,107 9,107" fill="#1a6fd0" opacity="0.8"/>
      <polygon points="284,233 615,233 615,305 243,305" fill="#d92a2a" opacity="0.92"/>
    </svg>
    <div class="hero-headline">
      <div class="kicker">Ready For</div>
      <div class="title">A beautiful &amp; Functional</div>
      <div class="title yellow">Kitchen <span class="or">or</span> Bathroom?</div>
    </div>
    <div class="hero-tagline">
      <div class="big">Work with a top-rated</div>
      <div class="sub">Local remodeling company in Brookdale, IA</div>
    </div>
  </section>
  <div class="hero-rule"></div>

  <section class="service" style="left:79px; top:454px;">
    <svg class="service-icon" width="28" height="28" viewBox="0 0 28 28" fill="none" stroke="#2272bb" stroke-width="0.8">
      <rect x="1" y="13" width="26" height="13"/><rect x="4" y="16" width="9" height="7"/><rect x="15" y="16" width="9" height="7"/>
      <circle cx="7" cy="8" r="2.5"/><line x1="4" y1="3" x2="10" y2="3"/><path d="M17 6h8l-2-3h-4z"/>
    </svg>
    <h2>KITCHEN REMODELING</h2>
    <p>Whatever your vision is for your new kitchen, our<br>crew can help you bring it to life. You can trust us for:</p>
    <ul>
      <li>Open concept design services</li><li>Kitchen cabinet installation services</li><li>Kitchen countertop installation services</li>
      <li>Tile installation services</li><li>Lighting installation services</li><li>Plumbing upgrade sservices</li>
      <li>Electrical upgrade services</li><li>Drywassll services</li><li>Painting services</li>
    </ul>
  </section>
  <div class="service-photo photo-framed photo-kitchen" style="left:203px; top:531px; width:113px; height:72px;" role="img" aria-label="White kitchen with island and wooden stools"></div>

  <section class="service" style="left:364px; top:454px;">
    <svg class="service-icon" width="28" height="28" viewBox="0 0 28 28" fill="none" stroke="#2272bb" stroke-width="0.8">
      <rect x="1" y="13" width="26" height="13"/><rect x="4" y="16" width="9" height="7"/><rect x="15" y="16" width="9" height="7"/>
      <circle cx="7" cy="8" r="2.5"/><line x1="4" y1="3" x2="10" y2="3"/><path d="M17 6h8l-2-3h-4z"/>
    </svg>
    <h2>HOME ADDITIONS</h2>
    <p>Whatever your vision is for your new kitchen, our<br>crew can help you bring it to life. You can trust us for:</p>
    <ul>
      <li>Open concept design services</li><li>Kitchen cabinet installation services</li><li>Kitchen countertop installation services</li>
      <li>Tile installation services</li><li>Lighting installation services</li><li>Plumbing upgrade sservices</li>
      <li>Electrical upgrade services</li><li>Drywassll services</li><li>Painting services</li>
    </ul>
  </section>
  <div class="service-photo photo-addition" style="left:506px; top:534px; width:112px; height:71px;" role="img" aria-label="Sunroom addition with vaulted wood ceiling"></div>

  <section class="service" style="left:79px; top:615px;">
    <svg class="service-icon" width="28" height="28" viewBox="0 0 28 28" fill="none" stroke="#2272bb" stroke-width="0.8">
      <rect x="1" y="13" width="26" height="13"/><rect x="4" y="16" width="9" height="7"/><rect x="15" y="16" width="9" height="7"/>
      <circle cx="7" cy="8" r="2.5"/><line x1="4" y1="3" x2="10" y2="3"/><path d="M17 6h8l-2-3h-4z"/>
    </svg>
    <h2>BATHROOM REMODELING</h2>
    <p>Whatever your vision is for your new kitchen, our<br>crew can help you bring it to life. You can trust us for:</p>
    <ul>
      <li>Open concept design services</li><li>Kitchen cabinet installation services</li><li>Kitchen countertop installation services</li>
      <li>Tile installation services</li><li>Lighting installation services</li><li>Plumbing upgrade sservices</li>
      <li>Electrical upgrade services</li><li>Drywassll services</li><li>Painting services</li>
    </ul>
  </section>
  <div class="service-photo photo-framed photo-bath" style="left:202px; top:726px; width:113px; height:73px;" role="img" aria-label="Remodeled bathroom with stone shower and tub"></div>

  <section class="service" style="left:364px; top:616px;">
    <svg class="service-icon" width="28" height="28" viewBox="0 0 28 28" fill="none" stroke="#2272bb" stroke-width="0.8">
      <rect x="1" y="13" width="26" height="13"/><rect x="4" y="16" width="9" height="7"/><rect x="15" y="16" width="9" height="7"/>
      <circle cx="7" cy="8" r="2.5"/><line x1="4" y1="3" x2="10" y2="3"/><path d="M17 6h8l-2-3h-4z"/>
    </svg>
    <h2>DECKS/PATIOS</h2>
    <p>Whatever your vision is for your new kitchen, our<br>crew can help you bring it to life. You can trust us for:</p>
    <ul>
      <li>Open concept design services</li><li>Kitchen cabinet installation services</li><li>Kitchen countertop installation services</li>
      <li>Tile installation services</li><li>Lighting installation services</li><li>Plumbing upgrade sservices</li>
      <li>Electrical upgrade services</li><li>Drywassll services</li><li>Painting services</li>
    </ul>
  </section>
  <div class="service-photo photo-deck" style="left:505px; top:729px; width:111px; height:70px;" role="img" aria-label="Backyard deck and patio with lounge chairs"></div>

  <footer class="footer">www.northvalehomes.com</footer>
</main>
</body>
</html>
```